Membership card Design

Hi I need a new membership card design for a social University club located in New Zealand. Our club name is called Maple Crest Society (MCSOC) and we provide a social hub for international students from Asia to meet local students. We are a non-profit organization that organizes activities such as paintball, ski trips, parties and day trips for our members. We need designs that look more like a membership card than a name card because we will be giving them to our members as a proof of membership. We would prefer a design that is simple in the front and with our club details, contacts and a place to write down a membership number on the back. We would like our card to have designs using the colours red, black, grey and orange. The design must incoporate the logo attached in this project. If possible, we would like the flower in the Hong Kong Flag to be incoporated in the design. The final design must look more like a membership card than a name card and communicate professionalism and high quality.

Target Market(s)

University Students

Industry/Entity Type

Non-Profit

Requirements
Must have
• The design must include:

The logo of our club
Our facebook page details: www.friendspage.example/maplecrest.soc
Our email: maplecrestsoc@mailbox.example
A place behind the card to print membership numbers.

```html
<!DOCTYPE html>
<html lang="en">
<head>
<meta charset="utf-8">
<title>Maple Crest Society – Membership Card</title>
<link rel="stylesheet" href="https://fonts.googleapis.com/css2?family=Marcellus+SC&family=Marcellus&display=swap">
<style>
  :root {
    --page-bg: #ececec;
    --card-light: #ffffff;
    --card-sheen: #f4f4f4;
    --card-shade: #d6d6d6;
    --brand-red: #d6202a;
    --deep-red: #8f0f16;
    --accent-orange: #e0782a;
    --steel-grey: #9a9a9a;
    --ink: #2a2a2a;
  }
  * { box-sizing: border-box; margin: 0; padding: 0; }
  html, body { width: 1200px; height: 787px; overflow: hidden; }
  body {
    background: var(--page-bg);
    display: flex;
    align-items: center;
    justify-content: center;
    gap: 60px;
  }
  .card {
    position: relative;
    width: 520px;
    height: 300px;
    border-radius: 4px;
    overflow: hidden;
    background: linear-gradient(100deg, var(--card-shade) 0%, var(--card-light) 38%, var(--card-sheen) 60%, var(--card-shade) 100%);
    box-shadow: 0 6px 18px rgba(0,0,0,0.18);
  }

  /* Decorative shard areas: soft gradient fills confined to the corners */
  .shard-area { position: absolute; pointer-events: none; }
  .card-front .shard-area.main {
    left: 0; bottom: 0; width: 170px; height: 200px;
    background:
      radial-gradient(ellipse 100% 100% at 0% 100%, rgba(143,15,22,0.95) 0%, rgba(214,32,42,0.85) 35%, rgba(224,120,42,0.55) 62%, rgba(224,120,42,0) 100%);
  }
  .card-front .shard-area.corner {
    right: 0; top: 0; width: 110px; height: 90px;
    background:
      radial-gradient(ellipse 100% 100% at 100% 0%, rgba(143,15,22,0.9) 0%, rgba(214,32,42,0.75) 35%, rgba(224,120,42,0.45) 65%, rgba(224,120,42,0) 100%);
  }
  .card-back .shard-area.main {
    left: 0; bottom: 0; width: 240px; height: 300px;
    background:
      radial-gradient(ellipse 100% 100% at 0% 100%, rgba(143,15,22,0.95) 0%, rgba(214,32,42,0.85) 30%, rgba(224,120,42,0.6) 55%, rgba(170,170,170,0.35) 78%, rgba(170,170,170,0) 100%);
  }

  .club-wordmark {
    position: absolute;
    display: flex;
    align-items: center;
    gap: 10px;
    font-family: "Marcellus SC", serif;
    color: var(--brand-red);
    white-space: nowrap;
    line-height: 1;
  }
  .club-wordmark .mark-dot {
    border-radius: 50%;
    background: var(--brand-red);
    flex: none;
  }
  .card-front .club-wordmark { left: 196px; top: 118px; font-size: 28px; }
  .card-front .club-wordmark .mark-dot { width: 32px; height: 32px; }

  .card-back .club-wordmark.faint {
    right: 22px; bottom: 18px; font-size: 14px; color: var(--steel-grey); gap: 6px;
  }
  .card-back .club-wordmark.faint .mark-dot { width: 14px; height: 14px; background: var(--steel-grey); }

  .contact-list {
    position: absolute;
    right: 22px;
    top: 34px;
    list-style: none;
    text-align: right;
    font-family: "Marcellus", serif;
    font-size: 14px;
    line-height: 26px;
    color: var(--deep-red);
    white-space: nowrap;
  }
  .member-number {
    position: absolute;
    right: 22px;
    top: 104px;
    display: flex;
    align-items: flex-end;
    gap: 14px;
  }
  .member-number .flower-marker {
    width: 18px; height: 18px; border-radius: 50%; background: var(--deep-red);
  }
  .member-number .write-line {
    width: 160px; border-bottom: 1.5px solid var(--brand-red);
  }
</style>
</head>
<body>
  <section class="card card-front" aria-label="Membership card front">
    <div class="shard-area main" role="img" aria-label="Angular red, orange and grey shard burst decoration"></div>
    <div class="shard-area corner" role="img" aria-label="Small red and orange shard burst decoration"></div>
    <div class="club-wordmark"><span class="mark-dot"></span><span>Maple Crest Soc</span></div>
  </section>

  <section class="card card-back" aria-label="Membership card back">
    <div class="shard-area main" role="img" aria-label="Large angular red, orange and grey shard burst decoration"></div>
    <ul class="contact-list">
      <li>www.friendspage.example/maplecrest.soc</li>
      <li>maplecrestsoc@mailbox.example</li>
    </ul>
    <div class="member-number" aria-label="Membership number">
      <span class="flower-marker" role="img" aria-label="Flower emblem"></span>
      <span class="write-line"></span>
    </div>
    <div class="club-wordmark faint"><span class="mark-dot"></span><span>Maple Crest Soc</span></div>
  </section>
</body>
</html>
```